Compelling Home Page for Clip Harbor Partners

We are a Video SEO specialist that get websites on top of the front page of Zentrova and FlickBarn with video thumbprints that generate great traffic. Video SEO is all we do

see what we're offering at a salespage www.plumfieldreels.example. However, please omit "guarantee"

he home page should introduce our company as a premier company for helping brands get their videos on the front page of zentrova and high up in flickbarn. Should incorporate video "thumbnails" as part of the design. These could be the "triangular click buttons" or little video screens you see as "thumbnails" Needs a prominent place for a video about videoSEO. on Left side of page towards the top.

Needs buttons across the top for other pages. See www.brastonclips.example for frame of reference we want to be better than them.

Must incorporate our logo. We'd like to see the logo on dark background as well as white background.

Simple but with bright and vibrant highlights that look sophisticated, cutting edge and accountable. Shows credentials. Links with examples of thumbnails that are on the front page

We want to beat www.brastonclips.example check it out for point of reference

Target Market(s)

large corporations who have videos already and want to get better traction. Marlow 500. Advertising Agencies for Marlow 500's

Requirements
Must have
• Incorporate our logo. clean, easy to read

```html
<!DOCTYPE html>
<html lang="en">
<head>
<meta charset="utf-8">
<title>Clip Harbor Partners – Video SEO</title>
<link rel="stylesheet" href="https://fonts.googleapis.com/css2?family=Arimo:wght@400;700&family=Arvo&family=Open+Sans:wght@600;700&display=swap">
<style>
:root{
  --black:#000;
  --ink:#1a1a1a;
  --blue-link:#2f3fa8;
  --nav-blue:#1f3fae;
  --yellow:#f7c600;
  --orange:#f08a00;
  --red-dark:#7a2a12;
  --red-mid:#b4542a;
  --panel-blue:#7ba9c3;
  --teal:#1c5559;
  --grey-page:#ecebea;
  --green:#3faa24;
  --green-light:#7fd657;
  --sky-link:#3aa0e0;
}
*{box-sizing:border-box;margin:0;padding:0}
html,body{width:1082px;height:1200px;overflow:hidden}
body{position:relative;background:var(--grey-page);font-family:"Arimo",Arial,sans-serif;color:var(--ink)}
.abs{position:absolute}

/* hero band */
.hero-band{left:0;top:100px;width:1082px;height:370px;
  background:radial-gradient(ellipse at 50% 40%,#c66a3a 0%,var(--red-mid) 40%,var(--red-dark) 100%)}
.steps-band{left:0;top:468px;width:1082px;height:620px;
  background:linear-gradient(180deg,#dcdad8 0%,#f4f3f2 40%,#fbfbfb 100%)}
.header-shape{left:0;top:0}

/* header */
.account-links{right:142px;top:2px;font-size:9px;color:var(--sky-link)}
.account-links span{color:#777;margin:0 3px}
.logo{left:141px;top:8px;width:200px;height:96px}
.logo .mark{position:absolute;left:62px;top:0;width:66px;height:66px;border-radius:50%;background:#1d1d1d;border:3px solid #e8a21c}
.logo .name{position:absolute;left:0;top:72px;width:200px;text-align:center;color:#fff;font-size:19px;font-weight:400;white-space:nowrap}
.engines{left:560px;top:30px;width:381px;height:58px;background:#fff;border-radius:7px;
  display:flex;align-items:center;justify-content:space-around;padding:0 10px}
.engines span{font-family:"Arimo",Arial,sans-serif;font-weight:700;font-size:17px;color:#3a3a3a}

/* nav */
.nav{left:329px;top:110px;display:flex;gap:31px}
.nav a{display:block;width:60px;height:50px;text-decoration:none;position:relative;background:#111}
.nav a::before,.nav a::after{content:"";position:absolute;left:4px;right:4px;height:3px;
  background:repeating-linear-gradient(90deg,#fff 0 4px,transparent 4px 8px)}
.nav a::before{top:2px}.nav a::after{bottom:2px}
.nav a span{position:absolute;left:2px;right:2px;top:8px;bottom:8px;background:linear-gradient(180deg,#fff,#e6e6e6);
  display:flex;align-items:center;justify-content:center;color:var(--nav-blue);font-weight:700;font-size:10px}

/* video */
.video{left:142px;top:182px;width:457px;height:278px;background:#fff;padding:4px}
.video .screen{width:449px;height:254px;background:linear-gradient(160deg,#8a7d6a 0%,#c9b593 35%,#3d3a4a 70%,#6b5a48 100%)}
.video .progress{height:2px;background:#ddd;position:relative}
.video .progress i{position:absolute;left:0;top:0;width:20px;height:2px;background:#c00}
.video .controls{height:16px;background:linear-gradient(#f4f4f4,#dcdcdc);display:flex;align-items:center;
  padding:0 6px;font-size:7px;color:#777;gap:8px}
.video .controls .grow{flex:1}
.video .controls b{display:inline-block;width:2px;height:8px;background:#999;margin-right:2px}

/* lead form */
.lead{left:607px;top:182px;width:333px;height:278px;background:#fff;padding:5px}
.lead .inner{position:relative;width:323px;height:268px;background:var(--panel-blue)}
.lead h2{position:absolute;left:0;top:16px;width:323px;text-align:center;font-size:12px;font-weight:700;color:#111}
.lead .hint{position:absolute;left:158px;top:30px;font-size:5.5px;color:#222}
.lead label{position:absolute;left:11px;font-size:9.5px;color:#111}
.lead .field{position:absolute;left:83px;width:88px;height:11px;background:#fff;border:1px solid #cfd9df}
.lead .msg{position:absolute;left:183px;top:41px;width:128px;height:60px;background:#fff;border:1px solid #cfd9df;font-size:7.5px;color:#999;padding:3px 4px}
.btn{position:absolute;height:27px;border-radius:14px;background:linear-gradient(180deg,var(--green-light),var(--green));
  color:#fff;font-family:"Arvo",Georgia,serif;font-size:12px;display:flex;align-items:center;padding-left:30px;gap:14px}
.btn .arrow{width:17px;height:17px;border-radius:50%;background:#1e3a12;display:flex;align-items:center;justify-content:center}
.lead .send{left:141px;top:129px;width:106px}
.promo{position:absolute;left:16px;top:150px;width:301px;height:94px;background:#000;border-radius:8px}
.promo .reel{position:absolute;left:12px;top:10px;width:100px;height:72px;border-radius:6px;background:radial-gradient(circle at 45% 50%,#e6e6e6 0%,#8a8a8a 45%,#2a1414 80%,#000 100%)}
.promo p{position:absolute;left:118px;top:28px;width:176px;text-align:center;color:#fff;font-family:"Arvo",Georgia,serif;font-size:15px;line-height:20px}
.lead .more{left:123px;top:231px;width:106px;padding-left:14px;gap:10px;font-size:11px}

/* steps */
.steps-title{left:0;top:490px;width:1082px;text-align:center;font-family:"Arvo",Georgia,serif;font-size:15px;color:#333}
.step{top:517px;width:246px;height:178px;background:#2a2a2a;padding:7px 4px;border:2px solid #cfcfcf}
.step .art{width:100%;height:100%;background:radial-gradient(ellipse at 50% 58%,#0e0e0e 0%,#1a1a14 28%,#d8d6c4 52%,#a6a482 100%)}
.step1{left:158px}.step2{left:418px}.step3{left:678px}

/* content cards */
.card{top:706px;height:372px;background:#fff;border:2px solid #d2d2d2;border-radius:7px;overflow:hidden}
.card h3{height:30px;padding:6px 10px;font-family:"Arvo",Georgia,serif;font-weight:400;font-size:15px;color:#fff;
  background:linear-gradient(90deg,var(--teal) 0%,#4d8b93 40%,rgba(255,255,255,0) 75%)}
.about{left:141px;width:585px}
.about .body{padding:6px 9px}
.about h4{font-family:"Arvo",Georgia,serif;font-weight:400;font-size:10.5px;color:var(--blue-link);margin-top:5px}
.about p{font-size:9.4px;line-height:18.3px;text-align:justify;margin-bottom:14px}
.quotes{left:732px;width:210px}
.quotes .body{padding:7px 9px;font-size:9.4px;line-height:18.3px;text-align:justify}
.quotes .who{font-family:"Arvo",Georgia,serif;font-size:10.5px}
.gap{height:18px}

/* footer */
.follow{left:144px;top:1135px;width:138px;height:38px;background:#2c2c2c;border:1px solid #555;border-radius:5px;
  display:flex;align-items:center;padding-left:8px;gap:5px;color:#ddd;font-family:"Open Sans",Arial,sans-serif;font-weight:700;font-size:7.5px}
.follow .label{margin-right:3px}
.follow i{display:block;width:14px;height:14px;border-radius:3px}
.footer-logo{left:483px;top:1140px;width:110px;height:50px}
.footer-logo .mark{position:absolute;left:28px;top:0;width:28px;height:28px;border-radius:50%;border:2px solid #b58520}
.footer-logo .name{position:absolute;left:0;top:33px;font-size:9.5px;color:#777;white-space:nowrap}
.footer-links{right:141px;top:1151px;font-family:"Open Sans",Arial,sans-serif;font-weight:600;font-size:9.5px;color:#fff}
.copyright{right:141px;top:1177px;font-size:7.5px;color:#ddd}
.copyright em{font-style:italic}
</style>
</head>
<body>

<div class="abs hero-band"></div>
<div class="abs steps-band"></div>

<svg class="abs header-shape" width="1082" height="190" viewBox="0 0 1082 190" aria-hidden="true">
  <path d="M0 0H1082V128C880 112 620 118 420 142C260 160 110 168 0 176Z" fill="#000"/>
  <path d="M0 178C110 170 260 162 420 144C620 120 880 114 1082 130" fill="none" stroke="var(--orange)" stroke-width="4"/>
  <path d="M0 174C110 166 260 158 420 140C620 116 880 110 1082 126" fill="none" stroke="var(--yellow)" stroke-width="5"/>
</svg>

<svg class="abs" style="left:0;top:1060px" width="1082" height="140" viewBox="0 0 1082 140" aria-hidden="true">
  <path d="M0 12C300 26 700 40 1082 20V140H0Z" fill="#000"/>
  <path d="M0 10C300 24 700 38 1082 18" fill="none" stroke="var(--yellow)" stroke-width="7"/>
  <path d="M0 16C300 30 700 44 1082 24" fill="none" stroke="var(--orange)" stroke-width="3"/>
  <path d="M0 5C300 19 700 33 1082 13" fill="none" stroke="#fff" stroke-width="3"/>
</svg>

<header>
  <div class="abs account-links">Sign in<span>|</span>Create new account</div>
  <div class="abs logo">
    <div class="mark"></div>
    <div class="name">Clip Harbor Partners</div>
  </div>
  <div class="abs engines">
    <span>FlickBarn</span><span>Vantor</span><span>Zentrova</span><span>Quibble</span>
  </div>
  <nav class="abs nav">
    <a href="#"><span>Home</span></a>
    <a href="#"><span>Services</span></a>
    <a href="#"><span>Examples</span></a>
    <a href="#"><span>Order</span></a>
    <a href="#"><span>Contact Us</span></a>
  </nav>
</header>

<section class="abs video">
  <div class="screen" role="img" aria-label="Video still of a business team meeting around a laptop and projector"></div>
  <div class="progress"><i></i></div>
  <div class="controls"><span><b></b><b></b></span><span>&#9834;</span><span>0:03 / 1:25</span><span class="grow"></span><span>360p</span><span>&#x26F6;</span></div>
</section>

<section class="abs lead">
  <div class="inner">
    <h2>INCREASE SALES UP TO 400%?</h2>
    <div class="hint">Please fill-in all fields and submit.</div>
    <label style="top:47px">Name</label><div class="field" style="top:46px"></div>
    <label style="top:75px">Email Address</label><div class="field" style="top:74px"></div>
    <label style="top:103px">Mobile Number</label><div class="field" style="top:102px"></div>
    <div class="msg">Message</div>
    <div class="btn send">Send<span class="arrow"><svg width="9" height="9" viewBox="0 0 9 9"><path d="M1 4.5H7M4.5 2L7 4.5 4.5 7" stroke="#fff" stroke-width="1.6" fill="none"/></svg></span></div>
    <div class="promo">
      <div class="reel" role="img" aria-label="Film reel with unspooling film strip"></div>
      <p>Clip Harbor Partners<br>Starting at $299</p>
    </div>
    <div class="btn more">Learn More<span class="arrow"><svg width="9" height="9" viewBox="0 0 9 9"><path d="M1 4.5H7M4.5 2L7 4.5 4.5 7" stroke="#fff" stroke-width="1.6" fill="none"/></svg></span></div>
  </div>
</section>

<h2 class="abs steps-title">3 Easy Steps for Your Clip Harbor Partners</h2>
<div class="abs step step1"><div class="art" role="img" aria-label="Step 1 film frame: ink splash with the words Choose Your Pack"></div></div>
<div class="abs step step2"><div class="art" role="img" aria-label="Step 2 film frame: ink splash with the words Fill Out Form"></div></div>
<div class="abs step step3"><div class="art" role="img" aria-label="Step 3 film frame: ink splash with the words Enjoy The Traffic"></div></div>

<section class="abs card about">
  <h3>What is Clip Harbor Partners</h3>
  <div class="body">
    <h4>VIDEO IS 53X MORE LIKELY TO APPEAR IN THE TOP TEN ON ZENTROVA THAN A WEBSITE</h4>
    <p>Lorem ipsum dolor sit amet, consectetur adipiscing elit. Proin nunc nisi, lobortis ac consectetur quis, pretium eget diam. Donec a scelerisque neque. Mauris volutpat imperdiet felis vitae venenatis. In aliquam porttitor augue et interdum. Donec leo nisi, placerat sit amet suscipit at, dictum et est. Praesent viverra cursus nunc ut mollis.</p>
    <h4>VIDEO INCREASES CONVERSIONS</h4>
    <p>Donec metus nunc, tempor eu dignissim at, iaculis eu augue. Suspendisse felis leo, viverra non egestas aliquam, pharetra id turpis. Proin placerat pharetra mauris ac fringilla. Class aptent taciti sociosqu ad litora torquent per conubia nostra, per inceptos himenaeos.</p>
    <h4>PEOPLE WILL WATCH A VIDEO FOR ALMOST 4 MINUTES AND A WEBSITE LESS THAN 60 SECONDS</h4>
    <p>Phasellus varius massa vel libero adipiscing auctor suscipit orci sodales. Nullam et elit tincidunt nisl fermentum tempor a a nibh. Curabitur tincidunt tincidunt quam in rhoncus. Sed magna purus, lobortis eget viverra ac, varius at ipsum. Sed a sem tellus. Aenean tempus diam arcu. Sed tincidunt interdum gravida.</p>
    <h4>WHAT'S YOUR VIDEO STRATEGY?</h4>
    <p>In augue nibh, porta id rutrum id, fermentum sed nunc. Nam neque est, dignissim quis facilisis a, eleifend ut nunc. In hac habitasse platea dictumst. Vestibulum orci mauris, eleifend vitae viverra et, convallis eget elit.</p>
  </div>
</section>

<section class="abs card quotes">
  <h3>Clients Quotes</h3>
  <div class="body">
    <p>"Please get that on our website immediately! Love it, love it, love it! Awesome job to everyone involved!! ... I will absolutely be sending more clients your way!"<br>Corin</p>
    <div class="gap"></div>
    <p class="who">- Ashgrove Homes</p>
    <div class="gap"></div>
    <p>"Good Morning Gentleman,I just wanted to give KUDOS to the production of the latest video made on www.kettlebay.example .. In addition, the technical support from Tomas Is second to none... I love the way it was made and how it is displayed on the site.. I expect to place another order today.. "</p>
    <div class="gap"></div>
    <p class="who">Ned Halloway</p>
    <p class="who">- Brightwell Medical, LLC</p>
  </div>
</section>

<footer>
  <div class="abs follow"><span class="label">Follow Us:</span><i style="background:#4a8fd6"></i><i style="background:#3a5ba0"></i><i style="background:#f08a1c"></i><i style="background:#ccc"></i></div>
  <div class="abs footer-logo"><div class="mark"></div><div class="name">Clip Harbor Partners</div></div>
  <div class="abs footer-links">About Us | Jobs | Legal Information | FAQ | Ask a Question | Business Section | How it works</div>
  <div class="abs copyright">© Clip Harbor Partners . <em>All Rights Reserved.</em></div>
</footer>

</body>
</html>
```